New innovative Food Supplements for Women’s Health needs label design

We are launching a line of food supplements designed specifically for women’s health, and we need a standout label design that appeals to health-conscious women and communicates high quality, premium and trust.

Industry/Entity Type

Consumer products, pharmacy, online

Requirements
Must have
• One label design for one product - see details in brief

```html
<!DOCTYPE html>
<html lang="en">
<head>
<meta charset="utf-8">
<title>Veralune Radiant Skin – Label</title>
<link rel="stylesheet" href="https://fonts.googleapis.com/css2?family=Abel&family=Barlow+Condensed:wght@600;700&family=Montserrat:wght@700;800&display=swap">
<style>
  :root {
    --navy: #26205e;
    --violet: #4a2582;
    --pink: #ea145a;
    --pink-light: #f0306f;
    --ink: #1a0f1c;
    --white: #ffffff;
    --panel: #f1f1f3;
    --gold-dark: #b8862a;
    --gold-light: #f3d472;
    --canvas: #efeff1;
  }
  * { margin: 0; padding: 0; box-sizing: border-box; }
  html, body {
    width: 1200px; height: 1200px; overflow: hidden;
    background: var(--canvas);
  }
  .label {
    position: absolute;
    left: 170px; top: 50px;
    width: 860px; height: 1099px;
    display: block;
  }
  .brand-name {
    font-family: "Montserrat", sans-serif; font-weight: 800;
    font-size: 30px; fill: var(--ink); letter-spacing: 4px;
  }
  .product-title {
    font-family: "Montserrat", sans-serif; font-weight: 800;
    fill: var(--white);
  }
  .product-title--main { font-size: 78px; }
  .product-title--sub { font-size: 46px; letter-spacing: 6px; }
  .product-type {
    font-family: "Montserrat", sans-serif; font-weight: 700;
    font-size: 25px; fill: var(--white); letter-spacing: 2px;
  }
  .claim {
    font-family: "Abel", sans-serif;
    font-size: 24px; fill: var(--white); letter-spacing: 0.8px;
  }
  .claim-head {
    font-family: "Barlow Condensed", sans-serif; font-weight: 700;
    font-size: 25px; fill: var(--ink); letter-spacing: 1px;
  }
  .badge-ring { fill: var(--white); stroke: var(--violet); stroke-width: 2.5; }
  .badge-glyph { fill: none; stroke: var(--violet); stroke-width: 2.4; stroke-linecap: round; stroke-linejoin: round; }
  .badge-label {
    font-family: "Barlow Condensed", sans-serif; font-weight: 600;
    font-size: 14px; fill: var(--white);
  }
  .volume {
    font-family: "Barlow Condensed", sans-serif; font-weight: 700;
    font-size: 34px; fill: var(--white);
  }
</style>
</head>
<body>
<svg class="label" viewBox="0 0 591 755" xmlns="http://www.w3.org/2000/svg" role="group" aria-label="Veralune Radiant Skin liquid supplement label">
  <defs>
    <radialGradient id="label-ground" cx="50%" cy="30%" r="70%">
      <stop offset="0" stop-color="#5c2a8e"/>
      <stop offset="0.6" stop-color="#352270"/>
      <stop offset="1" stop-color="#26205e"/>
    </radialGradient>
    <linearGradient id="pink-band" x1="0" y1="0" x2="1" y2="0">
      <stop offset="0" stop-color="#f0306f"/>
      <stop offset="0.5" stop-color="#ea145a"/>
      <stop offset="1" stop-color="#e0125a"/>
    </linearGradient>
    <linearGradient id="gold-edge" x1="0" y1="0" x2="0" y2="1">
      <stop offset="0" stop-color="#b8862a"/>
      <stop offset="0.35" stop-color="#f3d472"/>
      <stop offset="0.65" stop-color="#b8862a"/>
      <stop offset="1" stop-color="#f3d472"/>
    </linearGradient>
  </defs>

  <rect class="label-ground" width="591" height="755" fill="url(#label-ground)"/>
  <rect class="claims-band" x="0" y="327" width="591" height="333" fill="url(#pink-band)"/>

  <g class="side-panel side-panel--left">
    <path d="M0 0 H8 C70 180 82 520 10 755 H0 Z" fill="var(--panel)"/>
    <path d="M8 0 C70 180 82 520 10 755" fill="none" stroke="url(#gold-edge)" stroke-width="7"/>
  </g>
  <g class="side-panel side-panel--right" transform="translate(591 0) scale(-1 1)">
    <path d="M0 0 H8 C70 180 82 520 10 755 H0 Z" fill="var(--panel)"/>
    <path d="M8 0 C70 180 82 520 10 755" fill="none" stroke="url(#gold-edge)" stroke-width="7"/>
  </g>

  <path class="brand-tab" d="M198 0 H398 V60 Q398 72 386 72 H210 Q198 72 198 60 Z" fill="var(--white)"/>
  <text class="brand-name" x="298" y="50" text-anchor="middle" textLength="160" lengthAdjust="spacingAndGlyphs">VERALUNE</text>

  <g class="product-name" text-anchor="middle">
    <text class="product-title product-title--main" x="296" y="180" textLength="400" lengthAdjust="spacingAndGlyphs">RADIANT</text>
    <text class="product-title product-title--sub" x="296" y="236" textLength="170" lengthAdjust="spacingAndGlyphs">SKIN</text>
  </g>

  <text class="product-type" x="296" y="305" text-anchor="middle" textLength="354" lengthAdjust="spacingAndGlyphs">LIQUID SUPPLEMENTS</text>

  <g class="claims" text-anchor="middle">
    <text class="claim" x="296" y="361">Clinically tested</text>
    <text class="claim" x="296" y="399">For Skin, Hair and Nails</text>
    <text class="claim" x="296" y="437" textLength="375" lengthAdjust="spacingAndGlyphs">Hydrolyzed Marine Collagen 11000 mg</text>
    <text class="claim-head" x="296" y="475" textLength="340" lengthAdjust="spacingAndGlyphs">Powerful anti-ageing combo:</text>
    <text class="claim" x="296" y="513">retinol + hyaluronic acid</text>
    <text class="claim-head" x="296" y="551" textLength="302" lengthAdjust="spacingAndGlyphs">Supportive multivitamins:</text>
    <text class="claim" x="296" y="589" textLength="310" lengthAdjust="spacingAndGlyphs">Vitamins Selenium, Silicon, MSM</text>
  </g>

  <path class="base-band" d="M14 660 H577 C574 700 570 730 581 755 H10 C20 730 17 700 14 660 Z" fill="var(--navy)"/>

  <g class="badge badge--non-gmo">
    <circle class="badge-ring" cx="192" cy="653" r="27"/>
    <path class="badge-glyph" d="M192 672 V646 M192 658 C182 656 178 648 179 640 C187 641 192 648 192 658 M192 654 C202 652 206 644 205 636 C197 637 192 644 192 654"/>
    <text class="badge-label" x="192" y="707" text-anchor="middle">Non-GMO</text>
  </g>
  <g class="badge badge--gelatin-free">
    <circle class="badge-ring" cx="284" cy="653" r="27"/>
    <path class="badge-glyph" d="M273 644 H295 L291 668 H277 Z M268 636 L300 670"/>
    <text class="badge-label" x="284" y="707" text-anchor="middle">Gelatin Free</text>
  </g>
  <g class="badge badge--vegan">
    <circle class="badge-ring" cx="390" cy="653" r="27"/>
    <path class="badge-glyph" d="M378 668 L402 638 M386 658 C380 652 380 646 384 642 C388 646 389 652 386 658 M393 649 C387 643 388 637 392 633 M386 658 C393 660 399 658 401 653 C395 651 390 653 386 658"/>
    <text class="badge-label" x="390" y="707" text-anchor="middle">Vegan Friendly</text>
  </g>

  <text class="volume" x="545" y="716" text-anchor="end">500ml</text>
</svg>
</body>
</html>
```